WEB PAGES DESIGN

We need a web design for a new company called "NUBRA42". Our major business is that provide Internet Data Center solution, such as: rack/colocation, bandwidth, dedicated server, cloud server, CDN, and so on.
Requirements of Design:
1. Home page layout can refer to index-content.jpg in the attachments, but not limited.
2. According to match logo colors to design colors of web pages, Logo in the attachments.
3. The web contents of home page in image of the index-content.jpg.
4. The successful bidder will need to design three banner.
Industry/Entity Type
Business

```html
<!DOCTYPE html>
<html lang="en">
<head>
<meta charset="utf-8">
<title>NUBRA42 – Home</title>
<link rel="stylesheet" href="https://fonts.googleapis.com/css2?family=Open+Sans:wght@700&family=Anton&display=swap">
<style>
  :root {
    --page-bg: #f7f7f7;
    --column-bg: #ffffff;
    --ink: #000000;
    --nav-active: #80ff00;
    --tile-green: #00ff00;
    --tile-text: #ffffff;
    --panel-grey: #999999;
    --panel-border: #222222;
    --hero-light: #b8b8b8;
    --hero-dark: #4a4a4a;
  }
  * { box-sizing: border-box; margin: 0; padding: 0; }
  html, body {
    width: 1200px;
    height: 675px;
    overflow: hidden;
    background: var(--page-bg);
  }
  .page {
    position: relative;
    width: 540px;
    height: 675px;
    margin: 0 auto;
    background: var(--column-bg);
    overflow: hidden;
  }
  .site-header {
    position: absolute;
    left: 30px;
    top: 12px;
    right: 18px;
    height: 56px;
    display: flex;
    align-items: flex-start;
  }
  .brand {
    display: flex;
    flex-direction: column;
    align-items: center;
    width: 46px;
    margin-top: 2px;
  }
  .brand-mark {
    width: 30px;
    height: 30px;
    background: var(--nav-active);
  }
  .brand-name {
    margin-top: 5px;
    font-family: "Open Sans", sans-serif;
    font-weight: 700;
    font-size: 8px;
    color: var(--ink);
    letter-spacing: 0.2px;
  }
  .main-nav {
    display: flex;
    margin-left: 8px;
  }
  .main-nav a {
    display: block;
    padding: 0 4px;
    height: 34px;
    line-height: 34px;
    font-family: "Open Sans", sans-serif;
    font-weight: 700;
    font-size: 14px;
    color: var(--ink);
    text-decoration: none;
    white-space: nowrap;
  }
  .main-nav a.is-active { background: var(--nav-active); }
  .hero {
    position: absolute;
    left: 20px;
    top: 106px;
    width: 499px;
    height: 252px;
    background: linear-gradient(180deg, var(--hero-light) 0%, #8a8a8a 35%, var(--hero-dark) 70%, #7a7a7a 100%);
  }
  .service-tile {
    position: absolute;
    width: 237px;
    height: 109px;
    background: var(--tile-green);
    display: flex;
    align-items: center;
    justify-content: center;
    text-align: center;
    font-family: "Anton", sans-serif;
    font-size: 33px;
    line-height: 42px;
    color: var(--tile-text);
  }
  .tile-dedicated { left: 20px;  top: 373px; }
  .tile-servers   { left: 283px; top: 373px; }
  .tile-rack      { left: 20px;  top: 503px; }
  .tile-reseller  { left: 283px; top: 503px; }
  .feature-panel {
    position: absolute;
    left: 20px;
    top: 629px;
    width: 501px;
    height: 120px;
    background: var(--panel-grey);
    border: 1px solid var(--panel-border);
    text-align: center;
  }
  .feature-title {
    margin-top: 22px;
    font-family: "Anton", sans-serif;
    font-size: 64px;
    line-height: 1;
    color: var(--tile-text);
  }
</style>
</head>
<body>
  <div class="page">
    <header class="site-header">
      <div class="brand">
        <div class="brand-mark"></div>
        <span class="brand-name">NUBRA42</span>
      </div>
      <nav class="main-nav">
        <a href="#">Home</a>
        <a href="#" class="is-active">Dedicated Servers</a>
        <a href="#">Hosting</a>
        <a href="#">Data centers</a>
        <a href="#">About US</a>
      </nav>
    </header>

    <div class="hero" role="img" aria-label="Banner photo: black and white desert landscape with a field of cacti"></div>

    <a class="service-tile tile-dedicated">Dedicated<br>Hosting</a>
    <a class="service-tile tile-servers">Servers<br>Hosting</a>
    <a class="service-tile tile-rack">Rack &amp;<br>BandWidth</a>
    <a class="service-tile tile-reseller">Reseller &amp;<br>Referral</a>

    <section class="feature-panel">
      <h2 class="feature-title">Our</h2>
    </section>
  </div>
</body>
</html>
```